Webbanner-Design tovila.at Webshop
Zielgruppe
Onlineshop für Haus + Garten
tovila.at
Aufgabenstellung
Benötigt wird ein neues Banner-Set
ein Allgemeines - warum bei tovila.at einkaufen
- günstige Preise durch Direktbezug ohne Zwischenhandel
- alle Artikel vorrätig - schnelle Lieferung
- Sichere Kaufabwicklung - Calvoro Seal
- Fachberatung und Service durch geschultes Peronal
sowie Banner für jede Hauptkategorie

```html
<!DOCTYPE html>
<html lang="de">
<head>
<meta charset="utf-8">
<title>tovila.at – Webshop</title>
<link href="https://fonts.googleapis.com/css2?family=Open+Sans:wght@400;600;700;800&display=swap" rel="stylesheet">
<style>
  :root{
    --link:#3a8fd6;
    --navy:#1f3f80;
    --blue-mid:#22519a;
    --blue-light:#2a64ad;
    --gold:#c9a45c;
    --gold-dark:#b89148;
    --nav-text:#555;
    --white:#fff;
    --dot:#444;
  }
  *{box-sizing:border-box;margin:0;padding:0}
  html,body{width:1200px;height:745px;overflow:hidden}
  body{position:relative;font-family:"Open Sans",sans-serif;background:var(--white)}
  .brand{position:absolute;left:55px;top:34px;display:flex;align-items:center;gap:8px}
  .brand-dot{width:18px;height:18px;background:var(--navy);border-radius:50%}
  .brand-name{font-size:28px;font-weight:700;color:var(--gold-dark);letter-spacing:-.5px}
  .seal{position:absolute;left:342px;top:36px;width:52px;height:52px;border-radius:50%;background:var(--navy);border:3px solid #eee;box-shadow:0 0 0 1px #ccc}
  .top-links{position:absolute;left:892px;top:14px;display:flex;font-size:12px;color:var(--link)}
  .top-links span{padding:0 6px;border-left:1px solid #ccc;line-height:17px}
  .top-links span:first-child{border-left:none;padding-left:0}
  .lang{position:absolute;left:1069px;top:13px;width:76px;height:21px;background:#3b3b3b;color:#fff;font-size:11.5px;border-radius:3px;display:flex;align-items:center;justify-content:center;gap:3px;border:1px solid #222}
  .search{position:absolute;left:676px;top:49px;width:242px;height:36px;border:1px solid #ccc;border-radius:3px;display:flex;overflow:hidden}
  .search-field{flex:1;font-size:13.5px;color:#999;padding:0 12px;line-height:34px}
  .search-btn{width:40px;background:#eee;border-left:1px solid #ccc;display:flex;align-items:center;justify-content:center}
  .account,.cart{position:absolute;top:65px;font-size:14px;color:var(--link);display:flex;align-items:center;gap:4px}
  .account{left:947px}
  .cart{left:1069px}
  .caret{width:0;height:0;border-left:4px solid transparent;border-right:4px solid transparent;border-top:4px solid currentColor;margin-left:4px}
  .main-nav{position:absolute;left:0;top:113px;width:1200px;height:58px;background:linear-gradient(#fff,#ececec)}
  .main-nav span{position:absolute;top:19px;font-size:13.5px;color:var(--nav-text);display:flex;align-items:center}
  .main-nav .caret{margin-left:2px;border-top-color:#666}
  .backdrop{position:absolute;left:0;top:171px;width:1200px;height:574px;background:linear-gradient(90deg,#5b7a8c 0%,#8fb3c6 20%,#c8dde6 50%,#8eb6c8 80%,#3f7f95 100%)}
  .panel{position:absolute;left:50px;top:185px;width:1100px;height:549px;background:var(--white)}
  .hero{position:absolute;left:73px;top:207px;width:1055px;height:439px;background:linear-gradient(135deg,var(--navy) 0%,var(--blue-mid) 50%,var(--blue-light) 100%);overflow:hidden}
  .hero-art{position:absolute;left:0;top:0}
  .kicker{position:absolute;left:38px;top:34px;font-size:16px;color:#fff}
  .kicker b{font-weight:700}
  .headline{position:absolute;left:37px;top:84px;font-size:36px;line-height:41px;font-weight:800;color:#fff}
  .features{position:absolute;left:38px;top:186px;list-style:none;font-size:23px;line-height:28.5px;font-weight:700;color:#fff}
  .features li{display:flex;align-items:center;gap:6px}
  .cta{position:absolute;left:38px;top:359px;width:155px;height:43px;background:var(--gold);color:#fff;font-size:12px;font-weight:700;display:flex;align-items:center;justify-content:center;letter-spacing:.3px}
  .price-badge{position:absolute;left:890px;top:274px;width:128px;height:128px;border-radius:50%;background:var(--gold);color:#fff;text-align:center;font-weight:700}
  .price-badge .lead{font-size:11.5px;line-height:17.5px;margin-top:37px}
  .price-badge .amount{font-size:25px;line-height:30px;font-weight:800}
  .dots{position:absolute;left:521px;top:686px;display:flex;gap:19px;align-items:center}
  .dots span{width:6px;height:6px;border-radius:50%;background:var(--dot)}
  .dots .active{width:10px;height:10px;background:#fff;border:2px solid var(--dot);margin:0 -2px}
</style>
</head>
<body>
  <div class="brand"><span class="brand-dot"></span><span class="brand-name">tovila.at</span></div>
  <div class="seal" role="img" aria-label="Calvoro Seal Gütesiegel"></div>

  <nav class="top-links"><span>News</span><span>Kontakt</span><span>Links</span></nav>
  <div class="lang">Deutsch<span class="caret" style="margin-left:1px"></span></div>

  <div class="search">
    <div class="search-field">Suchen</div>
    <div class="search-btn">
      <svg width="16" height="16" viewBox="0 0 16 16"><circle cx="6.5" cy="6.5" r="5" fill="none" stroke="#1f5fa0" stroke-width="2.2"/><line x1="10.2" y1="10.2" x2="14.5" y2="14.5" stroke="#1f5fa0" stroke-width="2.6" stroke-linecap="round"/></svg>
    </div>
  </div>
  <div class="account">
    <svg width="12" height="13" viewBox="0 0 12 13"><circle cx="6" cy="3.5" r="3.2" fill="#3a8fd6"/><path d="M0 13 Q0 7 6 7 Q12 7 12 13Z" fill="#3a8fd6"/></svg>
    Anmelden<span class="caret"></span>
  </div>
  <div class="cart">
    <svg width="14" height="12" viewBox="0 0 14 12"><path d="M0 1h2.5l2 7h7l1.8-5H4" fill="none" stroke="#3a8fd6" stroke-width="1.8"/><circle cx="5.5" cy="10.5" r="1.3" fill="#3a8fd6"/><circle cx="10.5" cy="10.5" r="1.3" fill="#3a8fd6"/></svg>
    0,00 €<span class="caret"></span>
  </div>

  <nav class="main-nav">
    <span style="left:64px">Badezimmer<i class="caret"></i></span>
    <span style="left:183px">Schwimmbecken<i class="caret"></i></span>
    <span style="left:328px">Schwimmbadzubehör<i class="caret"></i></span>
    <span style="left:505px">Sauna</span>
    <span style="left:572px">Heizung, Solar, Klima<i class="caret"></i></span>
    <span style="left:743px">Garten<i class="caret"></i></span>
    <span style="left:826px">Kabelkanal</span>
    <span style="left:923px">Whirlpoolzubehör<i class="caret"></i></span>
  </nav>

  <div class="backdrop" role="img" aria-label="Unscharfer Hintergrund mit Wasserfläche"></div>
  <div class="panel"></div>

  <section class="hero">
    <svg class="hero-art" width="1055" height="439" viewBox="0 0 1055 439" role="img" aria-label="Foto: Holzsauna mit Saunakübel und entspannender Frau im Bademantel">
      <defs>
        <linearGradient id="sauna-tone" x1="0" y1="0" x2="1" y2="1">
          <stop offset="0" stop-color="#9a6a35"/>
          <stop offset=".5" stop-color="#c68e4e"/>
          <stop offset="1" stop-color="#e3b57a"/>
        </linearGradient>
      </defs>
      <path d="M494 0 Q330 220 476 439 L1055 439 L1055 0Z" fill="#c9a45c"/>
      <path d="M522 0 Q360 220 502 439 L1055 439 L1055 0Z" fill="url(#sauna-tone)"/>
    </svg>

    <p class="kicker"><b>IHR FACHMANN</b> FÜR BAD, POOL UND MEHR</p>
    <h1 class="headline">FÜR IHR PERFEKTES<br>SAUNA-ERLEBNIS</h1>
    <ul class="features">
      <li><svg width="15" height="18" viewBox="0 0 15 18"><path d="M0 0h6l9 9-9 9H0l9-9z" fill="#c9a45c"/></svg>SAUNAÖFEN</li>
      <li><svg width="15" height="18" viewBox="0 0 15 18"><path d="M0 0h6l9 9-9 9H0l9-9z" fill="#c9a45c"/></svg>GENERATOREN</li>
      <li><svg width="15" height="18" viewBox="0 0 15 18"><path d="M0 0h6l9 9-9 9H0l9-9z" fill="#c9a45c"/></svg>ZUBEHÖR UVM.</li>
    </ul>
    <div class="cta">ENTDECKEN</div>

    <div class="price-badge">
      <p class="lead">HOCHWERTIGES<br>ZUBEHÖR AB NUR</p>
      <p class="amount">59,99€</p>
    </div>
  </section>

  <div class="dots"><span></span><span></span><span></span><span></span><span class="active"></span><span></span><span></span></div>
</body>
</html>
```